LED strip light bag design

We are brivane lighting, a LED strip manufacturer in China, We need a packaging design for our LED strip light, as the strip market is full of standard package, so we want to make our package special, and use color orange, black and grey

Target Market(s)

USA, Europe

Contact Information for Business Card

Colin Wu
Director
Shenzhen Brivane Lighting Co., Ltd.
Add: 3F, Haodong Ind. Zone, Wenpu Rd, Baiqiao, Shenzhen 518420 China
Tel: +86-139-4826 3074 Fax: +86-755-28394610
E-mail: colin.wu@brivane-example.com

Font styles to use
Sans Serif
Other font styles liked:
• Tw Cen MT Condensed

Colors

Designer to choose only greyscale colors for use in the design.

Requirements
Must have
• Must have instructions of how to use the strip and CAUTION
• Must have CE, RoHS UL, trash can, ISO9001 logo
Nice to have
• Nice to have a back ground pictures with a strip drawing.

```html
<!DOCTYPE html>
<html lang="en">
<head>
<meta charset="utf-8">
<title>Brivane Lighting – LED Strip Light Pouch</title>
<link rel="stylesheet" href="https://fonts.googleapis.com/css2?family=Michroma&family=Yellowtail&display=swap">
<style>
  :root {
    --page-bg: #ffffff;
    --pouch-dark: #3d3d3d;
    --pouch-dark-edge: #2f2f2f;
    --bubble-tone: #5a5a5a;
    --led-black: #0d0d0d;
    --glow-orange: #f07a1e;
    --band-orange: #d7621c;
    --band-orange-deep: #b94f12;
    --band-silver: #b9b9b9;
    --script-grey: #e2e2e2;
    --badge-dark: #1c1c1c;
  }
  * { margin: 0; padding: 0; box-sizing: border-box; }
  html, body {
    width: 1200px;
    height: 904px;
    overflow: hidden;
    background: var(--page-bg);
  }
  .canvas {
    position: relative;
    width: 1200px;
    height: 904px;
  }
  .pouch-face {
    position: absolute;
    left: 290px;
    top: 60px;
    width: 620px;
    height: 784px;
    border-radius: 10px;
    overflow: hidden;
    background: linear-gradient(180deg, var(--pouch-dark-edge) 0%, var(--pouch-dark) 22%, var(--pouch-dark) 100%);
  }
  .bubble-pattern {
    position: absolute;
    left: 90px;
    top: 110px;
    width: 440px;
    height: 470px;
    border-radius: 50%;
    background: radial-gradient(circle at 50% 50%, var(--bubble-tone) 0%, rgba(90,90,90,0.55) 45%, rgba(61,61,61,0) 72%);
  }
  .wave-band {
    position: absolute;
    inset: 0;
    width: 620px;
    height: 784px;
  }
  .product-title {
    position: absolute;
    left: 0;
    width: 620px;
    top: 238px;
    text-align: center;
    font-family: "Michroma", sans-serif;
    font-size: 118px;
    line-height: 1;
    letter-spacing: 2px;
    color: var(--led-black);
    text-shadow: 0 0 14px var(--glow-orange), 0 0 28px var(--glow-orange), 0 0 44px rgba(240,122,30,0.6);
  }
  .product-subtitle {
    position: absolute;
    left: 0;
    width: 620px;
    top: 392px;
    text-align: center;
    font-family: "Yellowtail", cursive;
    font-size: 92px;
    line-height: 1;
    color: var(--script-grey);
    transform: rotate(-6deg);
  }
  .cert-row {
    position: absolute;
    left: 0;
    width: 620px;
    top: 712px;
    display: flex;
    justify-content: center;
    align-items: center;
    gap: 14px;
  }
  .cert-badge { background: var(--badge-dark); }
  .cert-badge.round { width: 22px; height: 22px; border-radius: 50%; }
  .cert-badge.small { width: 18px; height: 16px; border-radius: 3px; }
  .cert-badge.tall { width: 18px; height: 26px; border-radius: 3px; }
  .cert-badge.square { width: 28px; height: 34px; border-radius: 3px; }
</style>
</head>
<body>
<main class="canvas">
  <section class="pouch-face">
    <div class="bubble-pattern" role="img" aria-label="Decorative pattern of soft grey overlapping circles"></div>

    <svg class="wave-band" viewBox="0 0 620 784" aria-hidden="true">
      <defs>
        <linearGradient id="orangeBand" x1="0" y1="0" x2="1" y2="0">
          <stop offset="0" stop-color="var(--band-orange-deep)"/>
          <stop offset="0.5" stop-color="var(--band-orange)"/>
          <stop offset="1" stop-color="var(--band-orange-deep)"/>
        </linearGradient>
      </defs>
      <path d="M0 582 C 140 700, 330 660, 620 478 L620 784 L0 784 Z" fill="var(--band-silver)"/>
      <path d="M0 598 C 140 716, 330 676, 620 494 L620 784 L0 784 Z" fill="url(#orangeBand)"/>
    </svg>

    <h1 class="product-title">LED</h1>
    <p class="product-subtitle">strip light</p>

    <div class="cert-row" aria-label="Certification marks">
      <span class="cert-badge small"></span>
      <span class="cert-badge round"></span>
      <span class="cert-badge tall"></span>
      <span class="cert-badge square"></span>
    </div>
  </section>
</main>
</body>
</html>
```